Reggie Vosburn - Free Personalised Health Consultation - "Every body walks its own path"

This flyer will be left on tables/seats at speaking events and seminars and used to attain leads.

Top half will have "SMS me for a FREE Personalised Health Consultation" and my picture (see www.reggievosburn.example and pick most engaging photo) and underneath my contact details. It must have lines with "Notes:" halfway down so people can take notes at the seminar and lines on the back with my contact details again and "Notes: with lines.

I am having a business card also being designed by Plotnest for same and would like the flyer and business card to carry a similar feel/look for consistency.

Below is the brief for the business card being designed:
Business Card for www.reggievosburn.example site. It is a trust site and I use it for 1:1 relatable connections. It is the one I use for building intimate 1:1 trust building and Exec Coaching Services and programs for high wealth individuals and corporates. I also have a commercial programmatic site of my personal health products and services and programs for main stream one to many. www.crossgenvitality.example that can also provoke thought for the www.reggievosburn.example business card. (mind you will get a separate business card for that site, but want to provide context). It has a logo which you may want to draw from in designing the reggievosburn business card which is personal and is about building my brand. There is also a reggievosburn personal KX page and reggievosburn business KX page. I am a Certified Talent Compass 4.1 Coach with Verrick and you can get a corporate brief of me on there to give you more context https://www.verricktalenthub.example/coach/en-us/directory?search=reggie

Target Market(s)

Exec, IT, Health conscious. Corporates wanting to run Health and Wellness programs. Those wanting to go from good to great. Millennials to Middleaged.

Industry/Entity Type

Health And Wellness

Font styles to use
Sans Serif
Other font styles liked:
• Arial and Calibri ok too

Colors

Designer to choose colors to be used in the design.

Requirements
Must have
• Picture of me - use best from www.reggievosburn.example or can send one you choose.
• Contact details like my buisness card being designed by you guys in separate project.
• Name: Reggie Vosburn
• email: reggie@reggievosburn.,example
• Phone: Australia +61 455 318 026 Singapore: +65 8342 1960
Nice to have
• Open to ideas

```html
<!DOCTYPE html>
<html lang="en">
<head>
<meta charset="utf-8">
<title>Reggie Vosburn – Free Personalised Health Consultation Flyer</title>
<link href="https://fonts.googleapis.com/css2?family=Oswald:wght@400;500&family=Archivo+Black&family=Open+Sans:wght@400;600;700&display=swap" rel="stylesheet">
<style>
  :root {
    --backdrop: #232323;
    --paper: #ffffff;
    --ink: #111111;
    --band-grey: #9b9b9b;
    --band-black: #000000;
    --text-light: #ffffff;
    --photo-light: #e6e6e6;
    --photo-dark: #5a5a5a;
  }
  * { margin: 0; padding: 0; box-sizing: border-box; }
  html, body { width: 1200px; height: 1200px; overflow: hidden; background: var(--backdrop); }
  .flyer {
    position: absolute; left: 246px; top: 115px; width: 681px; height: 954px;
    background: var(--paper); color: var(--ink); overflow: hidden;
    font-family: "Open Sans", Arial, sans-serif;
  }
  .hero-art { position: absolute; left: 0; top: 0; width: 681px; height: 500px; }
  .headline { position: absolute; left: 27px; top: 42px; font-family: "Oswald", Arial, sans-serif; font-weight: 500; line-height: 1; letter-spacing: -0.3px; }
  .headline .lead { font-size: 42px; display: block; }
  .headline .free { font-size: 94px; display: block; margin-top: -2px; line-height: 0.95; }
  .headline .rest { font-size: 42px; display: block; line-height: 1.22; margin-top: 2px; }
  .coach-name { position: absolute; left: 27px; top: 300px; font-family: "Archivo Black", Arial, sans-serif; font-size: 25px; letter-spacing: 0.6px; }
  .locations { position: absolute; left: 27px; top: 341px; font-size: 18.5px; line-height: 26.5px; }
  .contact { position: absolute; left: 27px; font-size: 18.5px; display: flex; align-items: center; gap: 12px; }
  .contact.email { top: 443px; }
  .contact.phone { top: 477px; }
  .contact svg { flex: none; }
  .about-band { position: absolute; left: 0; top: 519px; width: 681px; height: 215px; background: var(--band-grey); color: var(--text-light); padding: 16px 26px 0 26px; font-size: 11.2px; line-height: 16px; }
  .about-band p + p { margin-top: 16px; }
  .about-band p.tight { margin-top: 12px; padding-left: 2px; }
  .profile-band { position: absolute; left: 0; top: 734px; width: 681px; height: 175px; background: var(--band-black); color: var(--text-light); }
  .profile-portrait { position: absolute; left: 26px; top: 40px; width: 88px; height: 88px; border-radius: 50%; border: 2px solid var(--text-light); background: radial-gradient(circle at 50% 40%, #d8d8d8, #7a7a7a); }
  .profile-facts { position: absolute; left: 125px; top: 10px; width: 520px; font-size: 11.8px; line-height: 16px; }
  .profile-facts p { text-align: justify; margin-bottom: 7px; }
  .profile-facts strong { font-weight: 700; }
  .site-footer { position: absolute; left: 0; top: 909px; width: 681px; height: 45px; display: flex; justify-content: space-between; align-items: center; padding: 0 22px 0 21px; font-size: 13.5px; }
  .site-footer span { display: flex; align-items: center; gap: 6px; }
</style>
</head>
<body>
<main class="flyer">
  <svg class="hero-art" viewBox="0 0 681 500" aria-hidden="false">
    <defs>
      <linearGradient id="photoTone" x1="0" y1="0" x2="1" y2="1">
        <stop offset="0" stop-color="var(--photo-light)"/>
        <stop offset="0.55" stop-color="#a8a8a8"/>
        <stop offset="1" stop-color="var(--photo-dark)"/>
      </linearGradient>
    </defs>
    <polygon role="img" aria-label="Black and white photo of Reggie Vosburn smiling, seated in a suit on a bright verandah" points="411,0 681,0 681,458 329,211" fill="url(#photoTone)"/>
    <line x1="396" y1="0" x2="347" y2="135" stroke="var(--ink)" stroke-width="4"/>
    <line x1="407" y1="0" x2="354" y2="140" stroke="var(--ink)" stroke-width="3"/>
    <line x1="346" y1="247" x2="681" y2="480" stroke="var(--ink)" stroke-width="6"/>
  </svg>

  <h1 class="headline">
    <span class="lead">SMS me for a</span>
    <span class="free">FREE</span>
    <span class="rest">Personalised<br>Health Consultation</span>
  </h1>

  <h2 class="coach-name">Reggie Vosburn</h2>
  <p class="locations">Gold Coast/Brisbane, Queensland, Australia<br>Sydney, New South Wales, Australia<br>Singapore</p>

  <p class="contact email">
    <svg width="26" height="18" viewBox="0 0 26 18"><rect x="0" y="0" width="26" height="18" fill="var(--ink)"/><polyline points="1,1 13,10 25,1" fill="none" stroke="var(--paper)" stroke-width="2"/><line x1="1" y1="17" x2="10" y2="8" stroke="var(--paper)" stroke-width="1.6"/><line x1="25" y1="17" x2="16" y2="8" stroke="var(--paper)" stroke-width="1.6"/></svg>
    reggie@reggievosburn.example
  </p>
  <p class="contact phone">
    <svg width="26" height="26" viewBox="0 0 26 26"><circle cx="13" cy="13" r="12" fill="none" stroke="var(--ink)" stroke-width="1.6"/><path d="M8.5 7.5c1-1 2-0.8 2.6 0.3l1 1.8c0.4 0.8 0.2 1.4-0.5 2-0.5 0.4-0.4 0.9 0 1.5 0.8 1.2 1.6 2 2.6 2.6 0.6 0.4 1.1 0.4 1.5-0.1 0.6-0.7 1.2-0.9 2-0.5l1.8 1c1.1 0.6 1.2 1.6 0.3 2.6-1.5 1.6-4 1.3-6.6-0.9-1.7-1.4-3.3-3.3-4.4-5.2-1.2-2.2-1.3-4 -0.3-5.1z" fill="var(--ink)"/></svg>
    Australia +61 455 318 026 / Singapore: +65 8342 1960
  </p>

  <section class="about-band">
    <p>To realize the full benefits of strengths, it is critical that you focus on developing them completely. Partnering with a Verrick-Certified Strengths Coach can be the difference between simply knowing your strengths and truly living a strengths-based life.</p>
    <p>The coaches listed here are recognized by Verrick as being fully qualified to coach others using strengths-based development. Find a coach that best suits you and your needs, and contact him or her to begin the next chapter in your strengths journey.</p>
    <p class="tight">It is a trust site and I use it for 1:1 relatable connections. It is the one I use for building intimate 1:1 trust building and Exec Coaching Services and programs for high wealth individuals and corporates. I also have a commercial programmatic site of my personal health products and services and programs for main stream one to many. www.crossgenvitality.example</p>
  </section>

  <section class="profile-band">
    <div class="profile-portrait" role="img" aria-label="Round portrait photo of Reggie Vosburn"></div>
    <div class="profile-facts">
      <p><strong>Coaching Expertise :</strong> Career, Enterprise Business, Executive Coaching, Healthcare, Keynotes, Leadership, Managers, Personal Development, Sales, Small Business/Entrepreneurs, Students/Youth, Teams, Technology, Wellbeing</p>
      <p><strong>Coaching Availability :</strong> Taking on Additional Clients</p>
      <p><strong>Coaching Method :</strong> Coaching Packages, Corporate Training Programs (e.g. Your Location), In Person, Individual (In-Person, Phone or Kallvo), Keynote Speaker, Online Video Conference (e.g. Kallvo), Phone, Seminars &amp; Retreats, Workshops</p>
      <p><strong>Coaching Language :</strong> English</p>
    </div>
  </section>

  <footer class="site-footer">
    <span><svg width="11" height="11" viewBox="0 0 12 12"><circle cx="6" cy="6" r="5" fill="none" stroke="var(--ink)" stroke-width="1.2"/><line x1="1" y1="6" x2="11" y2="6" stroke="var(--ink)"/><ellipse cx="6" cy="6" rx="2.2" ry="5" fill="none" stroke="var(--ink)"/></svg>www.crossgenvitality.example</span>
    <span><svg width="11" height="11" viewBox="0 0 12 12"><circle cx="6" cy="6" r="5" fill="none" stroke="var(--ink)" stroke-width="1.2"/><line x1="1" y1="6" x2="11" y2="6" stroke="var(--ink)"/><ellipse cx="6" cy="6" rx="2.2" ry="5" fill="none" stroke="var(--ink)"/></svg>www.reggievosburn.example</span>
  </footer>
</main>
</body>
</html>
```